Design wine label. Brand name The Juniper

Wine label design for 'The Juniper'. A few varieties but example-

The Juniper Shiraz 2016 Bendigo 750ml, 14%alc/vol.

'The juniper' at top of label, image of sparrow then vintage, variety etc under image.

simple, yet striking and modern look.

Font styles to use
Script

Requirements
Must have
• Image of a sparrow
Nice to have
• Simple image, outline, cartoon or Lino print style. Some colour but not too busy

```html
<!DOCTYPE html>
<html lang="en">
<head>
<meta charset="utf-8">
<title>The Juniper Shiraz – Wine Label</title>
<link rel="stylesheet" href="https://fonts.googleapis.com/css2?family=Pinyon+Script&family=Cormorant+Garamond:wght@500&family=Cormorant+SC:wght@500&display=swap">
<style>
  :root {
    --page: #f4f4f2;
    --label-black: #0d0d0d;
    --label-red: #c9202c;
    --band-white: #fafafa;
    --art-dark: #141414;
    --art-mid: #2a2a2a;
    --text-light: #f2f2f2;
  }
  * { margin: 0; padding: 0; box-sizing: border-box; }
  html, body {
    width: 789px;
    height: 1200px;
    overflow: hidden;
    background: var(--page);
  }
  .canvas {
    position: relative;
    width: 789px;
    height: 1200px;
  }
  .wine-label {
    position: absolute;
    left: 74px;
    top: 200px;
    width: 640px;
    height: 800px;
    background: var(--label-black);
    overflow: hidden;
  }
  .label-frame {
    position: absolute;
    inset: 12px;
    border: 1.5px solid var(--label-red);
    z-index: 3;
    pointer-events: none;
  }
  .label-band {
    position: absolute;
    left: 0;
    top: 0;
    width: 640px;
    height: 800px;
    z-index: 1;
  }
  .brand-script {
    position: absolute;
    top: 40px;
    left: 0;
    width: 100%;
    text-align: center;
    font-family: "Pinyon Script", cursive;
    font-weight: 400;
    font-size: 80px;
    line-height: 100px;
    color: var(--label-red);
    z-index: 2;
  }
  .label-art {
    position: absolute;
    left: 160px;
    top: 225px;
    width: 320px;
    height: 220px;
    border-radius: 6px;
    background: radial-gradient(ellipse at 45% 50%, var(--art-mid) 0%, var(--art-dark) 70%);
    z-index: 2;
  }
  .variety {
    position: absolute;
    top: 560px;
    left: 0;
    width: 100%;
    text-align: center;
    font-family: "Cormorant Garamond", serif;
    font-weight: 500;
    font-size: 46px;
    line-height: 56px;
    letter-spacing: 2px;
    text-transform: uppercase;
    color: var(--label-red);
    z-index: 2;
  }
  .wine-details {
    position: absolute;
    top: 705px;
    left: 0;
    width: 100%;
    text-align: center;
    font-family: "Cormorant SC", serif;
    font-weight: 500;
    font-size: 22px;
    line-height: 30px;
    letter-spacing: 0.5px;
    color: var(--text-light);
    z-index: 2;
  }
  .wine-details .divider {
    display: inline-block;
    width: 1.5px;
    height: 30px;
    margin: 0 6px;
    background: var(--text-light);
    vertical-align: -8px;
  }
</style>
</head>
<body>
<main class="canvas">
  <section class="wine-label">
    <svg class="label-band" viewBox="0 0 640 800" aria-hidden="true">
      <path d="M0,190 L640,180 L640,480 Q320,520 0,495 Z" fill="var(--band-white)"/>
    </svg>
    <h1 class="brand-script">The Juniper</h1>
    <div class="label-art" role="img" aria-label="Black bird silhouette illustration with the brand name lettered across it"></div>
    <p class="variety">Shiraz</p>
    <p class="wine-details">2016 Bendigo<span class="divider"></span>750mL / 14%alc/vol</p>
    <div class="label-frame"></div>
  </section>
</main>
</body>
</html>
```